Heron Real Estate Business Card

We have a card but we are looking for someone to make this card into a high resolution card. We would love the background to pop a little more than it currently does.
We need TWO sides. Black and gold are a must. Keep it classy, sophisticated, and luxurious. The W logo is also a must.
The back side needs to be larger font. Also, our Chatterleaf is Heron Real Estate FL (the printer messed up and put a 4 there)

Target Market(s)

Luxury clients for real estate

Industry/Entity Type

Real Estate

Contact Information for Business Card

This is a luxury real estate team. We need classy, luxury card. We print with a team that uses gold foil so gold is must.

Requirements
Must have
• Black and Gold, W logo
• Contact info on card provided in images
• KPB and Homeguild logo

```html
<!DOCTYPE html>
<html lang="en">
<head>
<meta charset="utf-8">
<title>Heron Real Estate Business Card</title>
<link rel="stylesheet" href="https://fonts.googleapis.com/css2?family=Cinzel:wght@400;500&display=swap">
<style>
  :root {
    --backdrop: #1b1b1c;
    --card: #111112;
    --gold: #c9a046;
  }
  * { margin: 0; padding: 0; box-sizing: border-box; }
  html, body {
    width: 1200px;
    height: 720px;
    overflow: hidden;
    background: var(--backdrop);
  }
  .canvas {
    width: 1200px;
    height: 720px;
    display: flex;
    align-items: center;
    justify-content: center;
    gap: 60px;
    font-family: "Cinzel", serif;
    color: var(--gold);
  }
  .card {
    width: 504px;
    height: 288px;
    background: var(--card);
    box-shadow: 0 18px 40px rgba(0,0,0,0.55);
  }
  .card-front {
    border: 3px solid var(--gold);
    display: flex;
    flex-direction: column;
    align-items: center;
    justify-content: center;
    gap: 16px;
  }
  .brand-circle {
    width: 130px;
    height: 130px;
    border: 1.5px solid var(--gold);
    border-radius: 50%;
  }
  .brand-name {
    font-size: 16px;
    letter-spacing: 4px;
    text-transform: uppercase;
  }
  .card-back {
    display: flex;
    flex-direction: column;
    align-items: center;
    justify-content: center;
    text-align: center;
    text-transform: uppercase;
  }
  .agent-name {
    font-size: 21px;
    letter-spacing: 2.5px;
    line-height: 1.2;
  }
  .agent-title {
    font-size: 11px;
    letter-spacing: 1.5px;
    line-height: 1.6;
    margin-bottom: 14px;
  }
  .office, .phone, .email, .web {
    font-size: 13px;
    letter-spacing: 1.3px;
    line-height: 1.55;
  }
  .phone { margin-bottom: 14px; }
  .affiliations {
    display: flex;
    gap: 22px;
    margin-top: 16px;
  }
  .affiliation {
    display: flex;
    align-items: center;
    gap: 6px;
    font-size: 10px;
    letter-spacing: 1px;
  }
  .affiliation-mark {
    width: 14px;
    height: 14px;
    border: 1.2px solid var(--gold);
  }
</style>
</head>
<body>
  <main class="canvas">
    <section class="card card-front" aria-label="Card front">
      <div class="brand-circle"></div>
      <div class="brand-name">Heron Real Estate</div>
    </section>

    <section class="card card-back" aria-label="Card back">
      <div class="agent-name">Julian Marsh</div>
      <div class="agent-title">Luxury Real Estate Consultant</div>
      <div class="office">Crestline Metro</div>
      <div class="phone">239-555-0187</div>
      <div class="email">office@heronrealestatefl.com</div>
      <div class="web">www.heronrealestatefl.com</div>
      <div class="affiliations">
        <div class="affiliation"><span class="affiliation-mark"></span>KPB</div>
        <div class="affiliation"><span class="affiliation-mark"></span>Homeguild</div>
      </div>
    </section>
  </main>
</body>
</html>
```